The Gemstone Craft Studio Sales Business Card

The goal of this project is to create a interactive & effective business card design for SALES purposes with the intention to get customer on to our website and make a purchase or contact us about a product or service.
Website: WWW.FENWORKSHOP.COM
LocalListPro: https://g.page/FenWORKSHOP?gm
Pagebook & Snapgrid: @THEBRIMORECRAFTSTUDIO
Phone # & Text Message & Chatwire Message: +1(555) 418-2963
Email: HELLO@FENWORKSHOP.COM
Location: 2871 Marbury Lane Suite 412 Elmsworth, WL
(It would be necessary to have the appropriate ticker/icon for each social media platform as well as the location ticker and phone / messaging icons instead of spelling the words out.)
It is important to have the company logo and details but with an emphasis toward website. Feel free to also completely make one design your way and completely custom as you feel best.
The Gemstone Craft Studio is a Provider of Luxury Goods & Services such as: Custom Jewelry Design, Jewelry Repairs & Cleaning, Designer Jewelry, Luxury Gifts, 24 Karat Gold, 22 Karat Gold Jewelry, Diamond Jewelry, Insured Jewelry Appraisals, Loose Gemstones & Diamonds, Supporting Sustainability
Target Market(s)
People looking to invest in precious metals and gemstones as well as people looking to find a gift for a loved one for a special occasion. Customers looking to Custom Design Jewelry.
Contact Information for Business Card
Font styles to use
Other font styles liked:
- w.e you want
Colors
Designer to choose colors to be used in the design.
Requirements
Must have
- Website: WWW.FENWORKSHOP.COM
- LocalListPro: https://g.page/FenWORKSHOP?gm
- Pagebook & Snapgrid: @THEBRIMORECRAFTSTUDIO
- Phone # & Text Message & Chatwire Message: +1(555) 418-2963
- Email: HELLO@FENWORKSHOP.COM
- Location: 2871 Marbury Lane Suite 412 Elmsworth, WL
- (It would be necessary to have the appropriate ticker/icon for each social media platform as well as the location ticker and phone / messaging icons instead of spelling the words out.)
- It is important to have the company logo and details but with an emphasis toward website. Feel free to also completely make one design your way and completely custom as you feel best.
Nice to have
- The Gemstone Craft Studio is a Provider of Luxury Goods & Services such as: Custom Jewelry Design, Jewelry Repairs & Cleaning, Designer Jewelry, Luxury Gifts, 24 Karat Gold, 22 Karat Gold Jewelry, Diamond Jewelry, Insured Jewelry Appraisals, Loose Gemstones & Diamonds, Supporting Sustainability

```html
<!DOCTYPE html>
<html lang="en">
<head>
<meta charset="utf-8">
<title>The Gemstone Craft Studio – Business Card</title>
<link href="https://fonts.googleapis.com/css2?family=Roboto:ital,wght@0,400;0,500;1,700&display=swap" rel="stylesheet">
<style>
  :root {
    --brand-red: #ec1c24;
    --brand-gold: #f7c52b;
    --paper: #ffffff;
    --ink: #1a1a1a;
    --backdrop: #e4e4e4;
  }
  * { box-sizing: border-box; margin: 0; padding: 0; }
  html, body { width: 1200px; height: 802px; overflow: hidden; }
  body {
    background: var(--backdrop);
    font-family: "Roboto", Arial, sans-serif;
    position: relative;
  }
  .card {
    position: absolute;
    top: 274px;
    width: 442px;
    height: 265px;
    overflow: hidden;
  }
  .card--front { left: 136px; background: var(--paper); }
  .card--back { left: 624px; background: var(--brand-red); color: #fff; }

  .front__band { position: absolute; left: 0; top: 0; width: 49px; height: 100%; background: var(--brand-red); }
  .front__stripe { position: absolute; left: 49px; top: 0; width: 3px; height: 100%; background: var(--brand-gold); }

  .contact-row {
    position: absolute;
    left: 66px;
    display: flex;
    align-items: center;
    gap: 4px;
    font-size: 11.5px;
    color: var(--ink);
    white-space: nowrap;
  }
  .contact-row--handle { font-size: 10.5px; }
  .icon { width: 19px; height: 19px; flex: none; }
  .address { position: absolute; left: 66px; top: 128px; display: flex; gap: 4px; font-size: 12px; line-height: 16px; color: var(--ink); white-space: nowrap; }
  .messaging-icons { position: absolute; left: 65px; top: 179px; display: flex; gap: 2px; }
  .messaging-icons .icon { width: 18px; height: 18px; }
  .phone-number { position: absolute; left: 65px; top: 203px; font-size: 12px; color: var(--ink); }

  .brand-mark {
    position: absolute;
    left: 272px;
    top: 60px;
    width: 160px;
    text-align: center;
  }
  .brand-mark__dot { width: 44px; height: 44px; border-radius: 50%; background: var(--brand-gold); margin: 0 auto 16px; }
  .brand-mark__name { font-size: 21px; font-weight: 500; line-height: 25px; color: var(--brand-red); }

  .back__emblem {
    position: absolute;
    left: 30px;
    top: 62px;
    width: 110px;
    height: 110px;
    border-radius: 50%;
    background: var(--brand-gold);
  }
  .back__copy { position: absolute; left: 147px; top: 64px; width: 290px; white-space: nowrap; }
  .back__intro { font-size: 13px; font-weight: 700; font-style: italic; line-height: 16px; margin-bottom: 15px; }
  .back__services { font-size: 13px; line-height: 15.8px; }
</style>
</head>
<body>

<section class="card card--front" aria-label="Business card front">
  <div class="front__band"></div>
  <div class="front__stripe"></div>

  <div class="contact-row" style="top:24px">
    <svg class="icon" viewBox="0 0 20 20" aria-label="Website"><circle cx="10" cy="10" r="8.5" fill="none" stroke="var(--brand-red)" stroke-width="1.3"/><circle cx="10" cy="10" r="5" fill="none" stroke="var(--brand-red)" stroke-width="1.2"/><path d="M5 10h10M10 5c-2 3-2 7 0 10M10 5c2 3 2 7 0 10" fill="none" stroke="var(--brand-red)" stroke-width="1"/></svg>
    <span>WWW.FENWORKSHOP.COM</span>
  </div>
  <div class="contact-row" style="top:47px">
    <svg class="icon" viewBox="0 0 20 20" role="img" aria-label="LocalListPro"><circle cx="10" cy="10" r="8.5" fill="none" stroke="var(--brand-red)" stroke-width="1.3"/></svg>
    <span>https://g.page/FenWORKSHOP?gm</span>
  </div>
  <div class="contact-row contact-row--handle" style="top:70px">
    <svg class="icon" viewBox="0 0 20 20" role="img" aria-label="Pagebook"><circle cx="10" cy="10" r="8.5" fill="none" stroke="var(--brand-red)" stroke-width="1.3"/></svg>
    <span>@THEBRIMORECRAFTSTUDIO</span>
  </div>
  <div class="contact-row contact-row--handle" style="top:92px">
    <svg class="icon" viewBox="0 0 20 20" role="img" aria-label="Snapgrid"><circle cx="10" cy="10" r="8.5" fill="none" stroke="var(--brand-red)" stroke-width="1.3"/></svg>
    <span>@THEBRIMORECRAFTSTUDIO</span>
  </div>

  <div class="address">
    <svg class="icon" viewBox="0 0 20 20" aria-label="Location"><circle cx="10" cy="10" r="8.5" fill="none" stroke="var(--brand-red)" stroke-width="1.3"/><path d="M10 15s-3.5-3.8-3.5-6.2a3.5 3.5 0 0 1 7 0C13.5 11.2 10 15 10 15z" fill="none" stroke="var(--brand-red)" stroke-width="1.2"/><circle cx="10" cy="8.8" r="1.2" fill="var(--brand-red)"/></svg>
    <span>2871 Marbury Lane Suite<br>412 Elmsworth, WL</span>
  </div>

  <div class="messaging-icons">
    <svg class="icon" viewBox="0 0 20 20" aria-label="Phone"><circle cx="10" cy="10" r="8.5" fill="none" stroke="var(--brand-red)" stroke-width="1.3"/><path d="M7 5.5l1.6 2.3-1 1.1c.6 1.3 1.5 2.2 2.7 2.8l1.1-1 2.3 1.5-.8 1.8c-3.6-.3-6.4-3.2-6.8-6.8z" fill="none" stroke="var(--brand-red)" stroke-width="1.1"/></svg>
    <svg class="icon" viewBox="0 0 20 20" aria-label="Text message"><rect x="2" y="3" width="16" height="11" rx="2.5" fill="var(--brand-red)"/><path d="M6 14l-1 4 4-4z" fill="var(--brand-red)"/><circle cx="6.5" cy="8.5" r="1" fill="#fff"/><circle cx="10" cy="8.5" r="1" fill="#fff"/><circle cx="13.5" cy="8.5" r="1" fill="#fff"/></svg>
    <svg class="icon" viewBox="0 0 20 20" role="img" aria-label="Chatwire"><circle cx="10" cy="10" r="8.5" fill="none" stroke="var(--brand-red)" stroke-width="1.3"/></svg>
  </div>
  <div class="phone-number">+1(555) 418-2963</div>

  <div class="contact-row" style="top:228px">
    <svg class="icon" viewBox="0 0 20 20" aria-label="Email"><circle cx="10" cy="10" r="8.5" fill="none" stroke="var(--brand-red)" stroke-width="1.3"/><rect x="5.5" y="6.5" width="9" height="7" rx="1" fill="var(--brand-red)"/><path d="M5.8 7l4.2 3.3L14.2 7" fill="none" stroke="#fff" stroke-width="1"/></svg>
    <span style="font-size:12.5px">HELLO@FENWORKSHOP.COM</span>
  </div>

  <div class="brand-mark">
    <div class="brand-mark__dot"></div>
    <div class="brand-mark__name">The Gemstone<br>Craft Studio</div>
  </div>
</section>

<section class="card card--back" aria-label="Business card back">
  <div class="back__emblem"></div>
  <div class="back__copy">
    <p class="back__intro">The Gemstone Craft Studio is a Provider of<br>Luxury Goods &amp; Services such as:</p>
    <p class="back__services">Custom Jewelry Design, Jewelry Repairs &amp;<br>Cleaning, Designer Jewelry<br>Luxury Gifts, 24 Karat Gold, 22 Karat Gold<br>Jewelry, Diamond Jewelry<br>Insured Jewelry Appraisals, Loose Gemstones<br>&amp; Diamonds, Supporting Sustainability</p>
  </div>
</section>

</body>
</html>
```